Cutting Costs Quickly - A Weekend Money Plan

Nonfiction book about how to save on insurance. Almost one hundred measures and examples to reduce ones insurance costs.

Target Market(s)

Men/Women between 18 and 50

Industry/Entity Type

Insurance

```html
<!DOCTYPE html>
<html lang="en">
<head>
<meta charset="utf-8">
<title>Cutting Costs Quickly - A Weekend Money Plan</title>
<link rel="stylesheet" href="https://fonts.googleapis.com/css2?family=Montserrat:wght@800;900&display=swap">
<style>
  :root {
    --page-bg: #141110;
    --cover-wine: #3a0d14;
    --cover-deep: #1f0509;
    --fabric-red: #6e1422;
    --band: #3b0a12;
    --band-edge: #2a060c;
    --title-green: #2aa33b;
    --text-white: #f4f1ee;
    --chart-red: #c8161a;
    --chart-green: #2b8f3a;
  }
  * { margin: 0; padding: 0; box-sizing: border-box; }
  html, body {
    width: 1200px;
    height: 1031px;
    overflow: hidden;
    background: var(--page-bg);
  }
  .canvas {
    position: relative;
    width: 1200px;
    height: 1031px;
    display: flex;
    align-items: center;
    justify-content: center;
  }
  .book-cover {
    position: relative;
    width: 600px;
    height: 860px;
    background: var(--cover-deep);
    overflow: hidden;
  }
  .cover-photo {
    position: absolute;
    inset: 0;
    background:
      linear-gradient(100deg, transparent 38%, rgba(200,202,206,0.55) 46%, rgba(160,162,166,0.35) 54%, transparent 62%),
      radial-gradient(ellipse at 25% 12%, var(--fabric-red) 0%, transparent 55%),
      radial-gradient(ellipse at 80% 85%, #5a1019 0%, transparent 60%),
      linear-gradient(180deg, #4d0f18 0%, var(--cover-wine) 45%, var(--cover-deep) 100%);
  }
  .author-tag {
    position: absolute;
    left: 40px;
    top: 300px;
    padding: 8px 16px 7px;
    background: var(--band-edge);
    color: var(--text-white);
    font-family: "Montserrat", sans-serif;
    font-weight: 900;
    font-size: 26px;
    letter-spacing: 1.5px;
    text-transform: uppercase;
  }
  .title-band {
    position: absolute;
    left: 0;
    right: 0;
    top: 365px;
    height: 175px;
    background: var(--band);
    box-shadow: 0 0 0 1px var(--band-edge);
  }
  .chart-art {
    position: absolute;
    left: 32px;
    top: 22px;
    width: 190px;
    height: 130px;
    border-radius: 65px;
    background: linear-gradient(90deg, var(--chart-red) 0%, var(--chart-red) 50%, var(--chart-green) 100%);
    opacity: 0.9;
  }
  .book-title {
    position: absolute;
    left: 248px;
    top: 26px;
    right: 20px;
    font-family: "Montserrat", sans-serif;
    font-weight: 900;
    text-transform: uppercase;
    line-height: 1;
  }
  .title-accent {
    display: block;
    color: var(--title-green);
    font-size: 42px;
    letter-spacing: 1px;
  }
  .title-line {
    display: block;
    color: var(--text-white);
    font-size: 22px;
    letter-spacing: 1px;
    margin: 5px 0;
  }
</style>
</head>
<body>
<main class="canvas">
  <section class="book-cover">
    <div class="cover-photo" role="img" aria-label="Photograph of a steel blade resting on dark red patterned fabric"></div>
    <p class="author-tag">Author's Name</p>
    <div class="title-band">
      <div class="chart-art" role="img" aria-label="Red and green savings pie illustration"></div>
      <h1 class="book-title">
        <span class="title-accent">Cutting</span>
        <span class="title-line">Costs Quickly</span>
        <span class="title-line">A Weekend</span>
        <span class="title-accent">Money Plan</span>
      </h1>
    </div>
  </section>
</main>
</body>
</html>
```